Business Card - Professional Minimalist - Double sided

We appreciate minimalist logo/web/collateral designs that allow design to tell a story. We want to relay a professional image/approach but throwing in a splash of modern when we’re able so long as it’s not distracting. Think 75% classic corporate, 25% modern. Open to black or white design, not sure which might look the best.

Target Market(s)

Senior executives or related government affairs contacts within the agriculture, energy, and defense industries (i.e., potential clients) but located outside of Washington, DC. Most potential clients based in DC with be familiar with both of us and our shared history.

Industry/Entity Type

Consulting

Contact Information for Business Card

Name: Daniel R. Whitlock
Title: Co-Founder & Partner
Address: 418 Bramblewood Ave. SE | Suite 2716 | Washington, D.C. 20019
Phone: (202) 555-0187
Email: Daniel@HollerbyWhitlock.com

Font styles to use
Serif

Colors

Designer to choose only greyscale colors for use in the design.

Requirements
Must have
• Name: Daniel R. Whitlock
Phone: (202) 555-0187

```html
<!DOCTYPE html>
<html lang="en">
<head>
<meta charset="utf-8">
<title>Hollerby Whitlock Group – Business Card</title>
<link href="https://fonts.googleapis.com/css2?family=Crimson+Pro:wght@400;600&display=swap" rel="stylesheet">
<style>
  :root {
    --backdrop: #a7a8ac;
    --card: #000000;
    --brand-grey: #6b6b6b;
    --mark-grey: #9c9c9c;
    --name-grey: #5e5e5e;
    --text-white: #ffffff;
  }
  html, body {
    margin: 0;
    width: 1200px;
    height: 1200px;
    overflow: hidden;
    background: var(--backdrop);
  }
  .canvas {
    position: relative;
    width: 1200px;
    height: 1200px;
  }
  .card {
    position: absolute;
    left: 226px;
    width: 809px;
    height: 463px;
    background: var(--card);
  }
  .card--front { top: 111px; }
  .card--back  { top: 638px; }

  .brand {
    position: absolute;
    display: flex;
    align-items: center;
    gap: 16px;
  }
  .brand__square {
    background: var(--mark-grey);
    flex: none;
  }
  .brand__name {
    font-family: "Crimson Pro", serif;
    font-weight: 600;
    color: var(--brand-grey);
    text-transform: uppercase;
    letter-spacing: 0.04em;
    white-space: nowrap;
    line-height: 1;
  }
  .card--front .brand {
    left: 0; right: 0; top: 196px;
    justify-content: center;
  }
  .card--front .brand__square { width: 44px; height: 44px; }
  .card--front .brand__name { font-size: 42px; }

  .card--back .brand { left: 66px; top: 72px; gap: 12px; }
  .card--back .brand__square { width: 28px; height: 28px; }
  .card--back .brand__name { font-size: 27px; }

  .contact {
    position: absolute;
    left: 150px;
    top: 178px;
    font-family: "Crimson Pro", serif;
    color: var(--text-white);
    font-size: 19px;
    line-height: 25px;
  }
  .contact p { margin: 0; }
  .contact__name {
    font-weight: 600;
    font-size: 26px;
    line-height: 30px;
    color: var(--name-grey);
    text-transform: uppercase;
    letter-spacing: 0.01em;
  }
  .contact__title { font-size: 19px; }
  .contact__address { margin-top: 27px !important; }
  .contact__phone { margin-top: 27px !important; }
</style>
</head>
<body>
<main class="canvas">
  <section class="card card--front" aria-label="Card front">
    <div class="brand">
      <span class="brand__square" aria-hidden="true"></span>
      <span class="brand__name">Hollerby Whitlock Group</span>
    </div>
  </section>

  <section class="card card--back" aria-label="Card back">
    <div class="brand">
      <span class="brand__square" aria-hidden="true"></span>
      <span class="brand__name">Hollerby Whitlock Group</span>
    </div>
    <div class="contact">
      <p class="contact__name">Daniel R. Whitlock</p>
      <p class="contact__title">Co-Founder &amp; Partner</p>
      <p class="contact__address">418 Bramblewood Ave. SE | Suite 2716<br>Washington, D.C. 20019</p>
      <p class="contact__phone">(202) 555-0187</p>
      <p class="contact__email">Daniel@HollerbyWhitlock.com</p>
    </div>
  </section>
</main>
</body>
</html>
```